Annual Event PPT Template

We need a PowerPoint template to use for a big annual event we host. Attached is the logo we use for everything. You can also reference our website (listed below) and our letterhead for design inspiration.

Please be sure to include our contact information on all of the PPT slides:
1. Phone: 802-431-7296
2. Address: 342 Pebble Creek Road, Williston, VT 05495
3. Website: www.Corvalix.com

```html
<!DOCTYPE html>
<html lang="en">
<head>
<meta charset="utf-8">
<title>Corvalix – Annual Event Presentation Template</title>
<link rel="stylesheet" href="https://fonts.googleapis.com/css2?family=Montserrat:wght@400;600;700;800&family=Open+Sans:wght@400;600&display=swap">
<style>
  :root {
    --board-dark: #8c8c8c;
    --board-light: #b3b3b3;
    --band: #a2a2a2;
    --white: #ffffff;
    --slide-top: #ffffff;
    --slide-bottom: #eceef0;
    --blue: #46749f;
    --blue-soft: #9bb7d3;
    --orange: #ef8a2a;
    --orange-soft: #f6b77a;
    --text-grey: #7b8088;
    --line-grey: #cfd3d8;
  }
  * { box-sizing: border-box; margin: 0; padding: 0; }
  html, body { width: 1200px; height: 3244px; overflow: hidden; }
  body {
    position: relative;
    font-family: "Open Sans", Arial, sans-serif;
    background: linear-gradient(90deg, var(--board-dark) 0 600px, var(--board-light) 600px 1200px);
  }

  /* header & section bands */
  .board-header { position: absolute; top: 0; height: 190px; width: 600px; display: flex; align-items: center; justify-content: center; text-align: center; }
  .board-header h1 { font-family: "Montserrat", Arial, sans-serif; font-weight: 800; font-size: 34px; line-height: 1.15; color: var(--white); letter-spacing: 1px; }
  .board-header.main { left: 0; }
  .board-header.sub { left: 600px; }
  .section-band { position: absolute; left: 0; width: 1200px; height: 44px; background: var(--band); display: flex; align-items: center; justify-content: center; font-family: "Montserrat", Arial, sans-serif; font-weight: 700; font-size: 26px; color: var(--white); }
  .side-label { position: absolute; left: 600px; width: 0; height: 0; }
  .side-label span { position: absolute; transform: translate(-50%, -50%) rotate(90deg); white-space: nowrap; font-family: "Montserrat", Arial, sans-serif; font-weight: 700; font-size: 24px; color: var(--white); }

  /* columns & slides */
  .column { position: absolute; top: 0; width: 540px; height: 3244px; }
  .column.main { left: 30px; }
  .column.sub { left: 630px; }
  .slide { position: absolute; left: 0; width: 540px; height: 304px; overflow: hidden; background: linear-gradient(180deg, var(--slide-top), var(--slide-bottom)); box-shadow: 0 2px 6px rgba(0,0,0,.18); }
  .sub .dots { opacity: .6; }

  .logo { position: absolute; left: 24px; top: 18px; display: flex; align-items: center; gap: 6px; font-family: "Montserrat", Arial, sans-serif; font-weight: 700; font-size: 20px; color: var(--blue); }
  .logo i { width: 10px; height: 10px; border-radius: 50%; background: var(--orange); display: block; }
  .title { position: absolute; font-family: "Montserrat", Arial, sans-serif; font-weight: 800; font-size: 17px; color: var(--blue); text-transform: uppercase; }
  .body { position: absolute; font-size: 7.5px; line-height: 1.5; color: var(--text-grey); }
  .footer { position: absolute; left: 0; bottom: 8px; width: 100%; text-align: center; font-size: 6px; color: var(--text-grey); }

  .dots { position: absolute; }
  .dots.tr { right: 0; top: 0; width: 170px; height: 120px; background: radial-gradient(ellipse at 100% 0%, rgba(239,138,42,.6) 0%, rgba(70,116,159,.35) 45%, rgba(70,116,159,0) 75%); }
  .dots.bl { left: 0; bottom: 0; width: 150px; height: 110px; background: radial-gradient(ellipse at 0% 100%, rgba(70,116,159,.5) 0%, rgba(239,138,42,.3) 45%, rgba(239,138,42,0) 75%); }
  .dots.left-tall { left: 0; top: 10px; width: 190px; height: 284px; background: radial-gradient(ellipse at 0% 50%, rgba(239,138,42,.55) 0%, rgba(70,116,159,.35) 45%, rgba(70,116,159,0) 75%); }
  .dots.br { right: 0; bottom: 0; width: 160px; height: 120px; background: radial-gradient(ellipse at 100% 100%, rgba(70,116,159,.45) 0%, rgba(239,138,42,.3) 45%, rgba(239,138,42,0) 75%); }

  .illustration { position: absolute; left: 30px; top: 80px; width: 170px; height: 150px; background: linear-gradient(160deg, #e4ecf4, #cbd9e7); border-radius: 4px; }
  .topics { position: absolute; left: 250px; top: 72px; width: 250px; list-style: none; }
  .topics li { font-size: 7.5px; color: var(--text-grey); margin-bottom: 10px; padding-left: 10px; position: relative; }
  .topics li::before { content: ""; position: absolute; left: 0; top: 3px; width: 5px; height: 5px; border-radius: 50%; background: var(--orange); }
  .topics b { color: var(--blue); font-weight: 700; }

  .photo { position: absolute; left: 70px; top: 50px; width: 150px; height: 190px; border: 5px solid var(--white); box-shadow: 0 1px 4px rgba(0,0,0,.2); background: linear-gradient(180deg, #d9dcdf, #a9b0b8); }
  .speaker-logo { position: absolute; left: 270px; top: 70px; font-family: "Montserrat", Arial, sans-serif; font-weight: 700; font-size: 24px; color: var(--blue); }
  .speaker-name { position: absolute; left: 270px; top: 122px; display: flex; align-items: center; gap: 8px; font-family: "Montserrat", Arial, sans-serif; font-weight: 800; font-size: 22px; color: var(--blue); }
  .speaker-line { position: absolute; left: 270px; font-size: 12px; color: var(--text-grey); display: flex; align-items: center; gap: 8px; }
  .speaker-line::before { content: ""; width: 14px; height: 2px; background: var(--orange); }

  .cover-logo { position: absolute; left: 0; top: 88px; width: 100%; text-align: center; font-family: "Montserrat", Arial, sans-serif; font-weight: 700; font-size: 50px; color: var(--blue); }
  .cover-name { position: absolute; left: 0; top: 170px; width: 100%; text-align: center; font-family: "Montserrat", Arial, sans-serif; font-weight: 600; font-size: 20px; color: var(--blue); }
  .contact { position: absolute; left: 320px; top: 222px; list-style: none; }
  .contact li { display: flex; align-items: center; gap: 6px; font-size: 8px; color: var(--text-grey); margin-bottom: 5px; }
  .contact svg { width: 10px; height: 10px; flex: none; }

  .image-box { position: absolute; background: var(--white); border: 1px solid var(--line-grey); }
  .numbered { position: absolute; left: 120px; top: 78px; width: 340px; list-style: none; }
  .numbered li { display: flex; gap: 14px; align-items: flex-start; margin-bottom: 14px; }
  .numbered .num { font-family: "Montserrat", Arial, sans-serif; font-weight: 800; font-size: 20px; color: var(--blue); line-height: 1; width: 18px; }
  .numbered p { font-size: 7.5px; line-height: 1.5; color: var(--text-grey); padding-top: 3px; }

  .chart { position: absolute; left: 190px; top: 70px; width: 260px; height: 210px; }
</style>
</head>
<body>

<header class="board-header main"><h1>PRESENTATION<br>MAIN VERSION</h1></header>
<header class="board-header sub"><h1>PRESENTATION<br>SUB VERSION</h1></header>

<div class="section-band" style="top:190px">introduce pages</div>
<div class="section-band" style="top:1302px">main page</div>
<div class="section-band" style="top:1702px">text pages</div>
<div class="section-band" style="top:2814px">graf pages</div>

<div class="side-label" style="top:768px"><span>introduce pages</span></div>
<div class="side-label" style="top:2280px"><span>text pages</span></div>
<div class="side-label" style="top:3036px"><span>graf pages</span></div>

<!-- two columns, identical structure -->
<div class="column main">
  <section class="slide intro-company" style="top:260px">
    <div class="dots tr" role="img" aria-label="Scattered orange and blue dots"></div>
    <div class="logo"><i></i>Corvalix</div>
    <div class="illustration" role="img" aria-label="Line drawing of a company building"></div>
    <h2 class="title" style="left:250px;top:42px">Introducing Company</h2>
    <p class="body" style="left:250px;top:72px;width:250px">Corvalix delivers managed IT support, network security and cloud services for growing businesses across the region, with a team that answers fast and plans ahead.</p>
    <p class="footer">802-431-7296 &nbsp;|&nbsp; 342 Pebble Creek Road, Williston, VT 05495 &nbsp;|&nbsp; www.Corvalix.com</p>
  </section>

  <section class="slide intro-presentation" style="top:616px">
    <div class="dots tr" role="img" aria-label="Scattered orange and blue dots"></div>
    <div class="logo"><i></i>Corvalix</div>
    <div class="illustration" role="img" aria-label="Line drawing of a presentation board"></div>
    <h2 class="title" style="left:250px;top:42px">Introducing Presentation</h2>
    <ul class="topics">
      <li><b>TOPIC 1:</b> Opening remarks and event goals</li>
      <li><b>TOPIC 2:</b> Year in review highlights</li>
      <li><b>TOPIC 3:</b> New services and partners</li>
      <li><b>TOPIC 4:</b> Customer success stories</li>
      <li><b>TOPIC 5:</b> Questions and closing notes</li>
    </ul>
    <p class="footer">802-431-7296 &nbsp;|&nbsp; 342 Pebble Creek Road, Williston, VT 05495 &nbsp;|&nbsp; www.Corvalix.com</p>
  </section>

  <section class="slide speaker" style="top:972px">
    <div class="dots tr" role="img" aria-label="Scattered orange and blue dots"></div>
    <div class="dots bl" role="img" aria-label="Scattered blue and orange dots"></div>
    <div class="photo" role="img" aria-label="Portrait photo of the presenter"></div>
    <div class="speaker-logo">Corvalix</div>
    <div class="speaker-name"><svg width="14" height="14" viewBox="0 0 14 14"><circle cx="7" cy="4.5" r="3" fill="#ef8a2a"/><path d="M1.5 13.5c0-3.2 2.5-5 5.5-5s5.5 1.8 5.5 5z" fill="#ef8a2a"/></svg>MY NAME</div>
    <div class="speaker-line" style="top:160px">my position</div>
    <div class="speaker-line" style="top:186px">about me, about presentation</div>
    <p class="footer">802-431-7296 &nbsp;|&nbsp; 342 Pebble Creek Road, Williston, VT 05495 &nbsp;|&nbsp; www.Corvalix.com</p>
  </section>

  <section class="slide cover" style="top:1372px">
    <div class="dots left-tall" role="img" aria-label="Scattered orange and blue dots"></div>
    <div class="dots tr" role="img" aria-label="Scattered orange and blue dots"></div>
    <div class="cover-logo">Corvalix</div>
    <div class="cover-name">Name Presentation</div>
    <ul class="contact">
      <li><svg viewBox="0 0 10 10"><path d="M5 0.5a3.3 3.3 0 0 0-3.3 3.3C1.7 6.3 5 9.5 5 9.5s3.3-3.2 3.3-5.7A3.3 3.3 0 0 0 5 0.5z" fill="#46749f"/><circle cx="5" cy="3.8" r="1.2" fill="#fff"/></svg>342 Pebble Creek Road<br>Williston, VT 05495</li>
      <li><svg viewBox="0 0 10 10"><path d="M2.2 0.8l1.6 1.9-1 1.2c.6 1.3 1.6 2.3 2.9 2.9l1.2-1 1.9 1.6-.9 1.8C4.6 9 1 5.4.4 1.7z" fill="#46749f"/></svg>802-431-7296</li>
      <li><svg viewBox="0 0 10 10"><circle cx="5" cy="5" r="4.2" fill="none" stroke="#46749f" stroke-width="1"/><path d="M.8 5h8.4M5 .8c-2.4 2.4-2.4 6 0 8.4M5 .8c2.4 2.4 2.4 6 0 8.4" fill="none" stroke="#46749f" stroke-width=".8"/></svg>www.Corvalix.com</li>
    </ul>
  </section>

  <section class="slide text-a" style="top:1772px">
    <div class="dots tr" role="img" aria-label="Scattered orange and blue dots"></div>
    <div class="dots bl" role="img" aria-label="Scattered blue and orange dots"></div>
    <div class="logo"><i></i>Corvalix</div>
    <h2 class="title" style="left:230px;top:30px">Text for Presentation</h2>
    <div class="image-box" style="left:40px;top:80px;width:150px;height:130px"></div>
    <p class="body" style="left:230px;top:62px;width:260px">Use this space to share the key message of the slide. Keep sentences short, focus on one idea and support it with a clear example or figure.</p>
    <p class="footer">802-431-7296 &nbsp;|&nbsp; 342 Pebble Creek Road, Williston, VT 05495 &nbsp;|&nbsp; www.Corvalix.com</p>
  </section>

  <section class="slide text-b" style="top:2128px">
    <div class="dots tr" role="img" aria-label="Scattered orange and blue dots"></div>
    <div class="logo"><i></i>Corvalix</div>
    <h2 class="title" style="left:40px;top:72px">Text for Presentation</h2>
    <p class="body" style="left:40px;top:102px;width:260px">Use this space to share the key message of the slide. Keep sentences short, focus on one idea and support it with a clear example or figure.</p>
    <div class="image-box" style="left:330px;top:150px;width:140px;height:110px"></div>
    <p class="footer">802-431-7296 &nbsp;|&nbsp; 342 Pebble Creek Road, Williston, VT 05495 &nbsp;|&nbsp; www.Corvalix.com</p>
  </section>

  <section class="slide text-c" style="top:2484px">
    <div class="dots tr" role="img" aria-label="Scattered orange and blue dots"></div>
    <div class="logo"><i></i>Corvalix</div>
    <h2 class="title" style="left:200px;top:30px">Text for Presentation</h2>
    <ol class="numbered">
      <li><span class="num">1.</span><p>Describe the first point here in two or three brief lines of supporting text.</p></li>
      <li><span class="num">2.</span><p>Describe the second point here in two or three brief lines of supporting text.</p></li>
      <li><span class="num">3.</span><p>Describe the third point here in two or three brief lines of supporting text.</p></li>
    </ol>
    <p class="footer">802-431-7296 &nbsp;|&nbsp; 342 Pebble Creek Road, Williston, VT 05495 &nbsp;|&nbsp; www.Corvalix.com</p>
  </section>

  <section class="slide graph" style="top:2884px">
    <div class="dots bl" role="img" aria-label="Scattered blue and orange dots"></div>
    <div class="dots tr" role="img" aria-label="Scattered orange and blue dots"></div>
    <div class="logo"><i></i>Corvalix</div>
    <h2 class="title" style="left:200px;top:40px">Text for Graf</h2>
    <svg class="chart" viewBox="0 0 260 210">
      <line x1="10" y1="195" x2="250" y2="195" stroke="#9bb7d3" stroke-width="1.5"/>
      <rect x="25" y="160" width="26" height="35" fill="#9bb7d3"/>
      <rect x="62" y="140" width="26" height="55" fill="#9bb7d3"/>
      <rect x="99" y="118" width="26" height="77" fill="#46749f"/>
      <rect x="136" y="95" width="26" height="100" fill="#46749f"/>
      <rect x="173" y="70" width="26" height="125" fill="#46749f"/>
      <rect x="210" y="45" width="26" height="150" fill="#46749f"/>
      <polyline points="20,140 70,118 110,96 150,72 190,48 232,18" fill="none" stroke="#ef8a2a" stroke-width="2.5"/>
      <polygon points="240,10 226,14 236,24" fill="#ef8a2a"/>
    </svg>
    <p class="footer">802-431-7296 &nbsp;|&nbsp; 342 Pebble Creek Road, Williston, VT 05495 &nbsp;|&nbsp; www.Corvalix.com</p>
  </section>
</div>

<div class="column sub">
  <section class="slide intro-company" style="top:260px">
    <div class="dots tr" role="img" aria-label="Scattered orange and blue dots"></div>
    <div class="logo"><i></i>Corvalix</div>
    <div class="illustration" role="img" aria-label="Line drawing of a company building"></div>
    <h2 class="title" style="left:250px;top:42px">Introducing Company</h2>
    <p class="body" style="left:250px;top:72px;width:250px">Corvalix delivers managed IT support, network security and cloud services for growing businesses across the region, with a team that answers fast and plans ahead.</p>
    <p class="footer">802-431-7296 &nbsp;|&nbsp; 342 Pebble Creek Road, Williston, VT 05495 &nbsp;|&nbsp; www.Corvalix.com</p>
  </section>

  <section class="slide intro-presentation" style="top:616px">
    <div class="dots tr" role="img" aria-label="Scattered orange and blue dots"></div>
    <div class="logo"><i></i>Corvalix</div>
    <div class="illustration" role="img" aria-label="Line drawing of a presentation board"></div>
    <h2 class="title" style="left:250px;top:42px">Introducing Presentation</h2>
    <ul class="topics">
      <li><b>TOPIC 1:</b> Opening remarks and event goals</li>
      <li><b>TOPIC 2:</b> Year in review highlights</li>
      <li><b>TOPIC 3:</b> New services and partners</li>
      <li><b>TOPIC 4:</b> Customer success stories</li>
      <li><b>TOPIC 5:</b> Questions and closing notes</li>
    </ul>
    <p class="footer">802-431-7296 &nbsp;|&nbsp; 342 Pebble Creek Road, Williston, VT 05495 &nbsp;|&nbsp; www.Corvalix.com</p>
  </section>

  <section class="slide speaker" style="top:972px">
    <div class="dots tr" role="img" aria-label="Scattered orange and blue dots"></div>
    <div class="dots bl" role="img" aria-label="Scattered blue and orange dots"></div>
    <div class="photo" role="img" aria-label="Portrait photo of the presenter"></div>
    <div class="speaker-logo">Corvalix</div>
    <div class="speaker-name"><svg width="14" height="14" viewBox="0 0 14 14"><circle cx="7" cy="4.5" r="3" fill="#ef8a2a"/><path d="M1.5 13.5c0-3.2 2.5-5 5.5-5s5.5 1.8 5.5 5z" fill="#ef8a2a"/></svg>MY NAME</div>
    <div class="speaker-line" style="top:160px">my position</div>
    <div class="speaker-line" style="top:186px">about me, about presentation</div>
    <p class="footer">802-431-7296 &nbsp;|&nbsp; 342 Pebble Creek Road, Williston, VT 05495 &nbsp;|&nbsp; www.Corvalix.com</p>
  </section>

  <section class="slide cover" style="top:1372px">
    <div class="dots left-tall" role="img" aria-label="Scattered orange and blue dots"></div>
    <div class="dots tr" role="img" aria-label="Scattered orange and blue dots"></div>
    <div class="cover-logo">Corvalix</div>
    <div class="cover-name">Name Presentation</div>
    <ul class="contact">
      <li><svg viewBox="0 0 10 10"><path d="M5 0.5a3.3 3.3 0 0 0-3.3 3.3C1.7 6.3 5 9.5 5 9.5s3.3-3.2 3.3-5.7A3.3 3.3 0 0 0 5 0.5z" fill="#46749f"/><circle cx="5" cy="3.8" r="1.2" fill="#fff"/></svg>342 Pebble Creek Road<br>Williston, VT 05495</li>
      <li><svg viewBox="0 0 10 10"><path d="M2.2 0.8l1.6 1.9-1 1.2c.6 1.3 1.6 2.3 2.9 2.9l1.2-1 1.9 1.6-.9 1.8C4.6 9 1 5.4.4 1.7z" fill="#46749f"/></svg>802-431-7296</li>
      <li><svg viewBox="0 0 10 10"><circle cx="5" cy="5" r="4.2" fill="none" stroke="#46749f" stroke-width="1"/><path d="M.8 5h8.4M5 .8c-2.4 2.4-2.4 6 0 8.4M5 .8c2.4 2.4 2.4 6 0 8.4" fill="none" stroke="#46749f" stroke-width=".8"/></svg>www.Corvalix.com</li>
    </ul>
  </section>

  <section class="slide text-a" style="top:1772px">
    <div class="dots tr" role="img" aria-label="Scattered orange and blue dots"></div>
    <div class="dots bl" role="img" aria-label="Scattered blue and orange dots"></div>
    <div class="logo"><i></i>Corvalix</div>
    <h2 class="title" style="left:230px;top:30px">Text for Presentation</h2>
    <div class="image-box" style="left:40px;top:80px;width:150px;height:130px"></div>
    <p class="body" style="left:230px;top:62px;width:260px">Use this space to share the key message of the slide. Keep sentences short, focus on one idea and support it with a clear example or figure.</p>
    <p class="footer">802-431-7296 &nbsp;|&nbsp; 342 Pebble Creek Road, Williston, VT 05495 &nbsp;|&nbsp; www.Corvalix.com</p>
  </section>

  <section class="slide text-b" style="top:2128px">
    <div class="dots tr" role="img" aria-label="Scattered orange and blue dots"></div>
    <div class="logo"><i></i>Corvalix</div>
    <h2 class="title" style="left:40px;top:72px">Text for Presentation</h2>
    <p class="body" style="left:40px;top:102px;width:260px">Use this space to share the key message of the slide. Keep sentences short, focus on one idea and support it with a clear example or figure.</p>
    <div class="image-box" style="left:330px;top:150px;width:140px;height:110px"></div>
    <p class="footer">802-431-7296 &nbsp;|&nbsp; 342 Pebble Creek Road, Williston, VT 05495 &nbsp;|&nbsp; www.Corvalix.com</p>
  </section>

  <section class="slide text-c" style="top:2484px">
    <div class="dots tr" role="img" aria-label="Scattered orange and blue dots"></div>
    <div class="logo"><i></i>Corvalix</div>
    <h2 class="title" style="left:200px;top:30px">Text for Presentation</h2>
    <ol class="numbered">
      <li><span class="num">1.</span><p>Describe the first point here in two or three brief lines of supporting text.</p></li>
      <li><span class="num">2.</span><p>Describe the second point here in two or three brief lines of supporting text.</p></li>
      <li><span class="num">3.</span><p>Describe the third point here in two or three brief lines of supporting text.</p></li>
    </ol>
    <p class="footer">802-431-7296 &nbsp;|&nbsp; 342 Pebble Creek Road, Williston, VT 05495 &nbsp;|&nbsp; www.Corvalix.com</p>
  </section>

  <section class="slide graph" style="top:2884px">
    <div class="dots bl" role="img" aria-label="Scattered blue and orange dots"></div>
    <div class="dots tr" role="img" aria-label="Scattered orange and blue dots"></div>
    <div class="logo"><i></i>Corvalix</div>
    <h2 class="title" style="left:200px;top:40px">Text for Graf</h2>
    <svg class="chart" viewBox="0 0 260 210">
      <line x1="10" y1="195" x2="250" y2="195" stroke="#9bb7d3" stroke-width="1.5"/>
      <rect x="25" y="160" width="26" height="35" fill="#9bb7d3"/>
      <rect x="62" y="140" width="26" height="55" fill="#9bb7d3"/>
      <rect x="99" y="118" width="26" height="77" fill="#46749f"/>
      <rect x="136" y="95" width="26" height="100" fill="#46749f"/>
      <rect x="173" y="70" width="26" height="125" fill="#46749f"/>
      <rect x="210" y="45" width="26" height="150" fill="#46749f"/>
      <polyline points="20,140 70,118 110,96 150,72 190,48 232,18" fill="none" stroke="#ef8a2a" stroke-width="2.5"/>
      <polygon points="240,10 226,14 236,24" fill="#ef8a2a"/>
    </svg>
    <p class="footer">802-431-7296 &nbsp;|&nbsp; 342 Pebble Creek Road, Williston, VT 05495 &nbsp;|&nbsp; www.Corvalix.com</p>
  </section>
</div>

</body>
</html>
```